Rebrand of 3 bottle labels for nail polish brand

The task is to make a rebranding of our current gel nail polish bottle design. We have become one of the leading european nail polish brand, so we want to improve the quality of the label design to a more scandinavian and minimalistic bottle design, which stille has to be recognisable and unique.

We have attached a more detailed description of the rebranding instructions for our gel polish bottles called "bottle task".
Updates

The Labels should not be just Black and White as stated. But should be mainly Black and White and then some of our color as explained in the uploaded file.

Target Market(s)

Girls and women age 18-55 Northern Europe

Industry/Entity Type

Cosmetic/ Nail Gel Polish

Colors

Designer to choose only greyscale colors for use in the design.

Requirements
Must have
• See attched design instruction
Nice to have
• Moderne, Minimalist, Recognizable and Unique look
Should not have
• Too many elements, too busy design

```html
<!DOCTYPE html>
<html lang="en">
<head>
<meta charset="utf-8">
<title>Velmora Base Coat Label</title>
<link rel="stylesheet" href="https://fonts.googleapis.com/css2?family=Poppins:wght@300;400;600&family=Kaushan+Script&display=swap">
<style>
  :root {
    --page: #ffffff;
    --label: #ffffff;
    --ink: #111111;
    --violet: #a274ec;
    --lavender: #8f8ef0;
    --wash: #cdf2f4;
    --splash: #9a90ec;
    --rule: #9a9a9a;
    --panel-grey: #e0e0e0;
    --leaf: #7cb84a;
  }
  * { margin: 0; padding: 0; box-sizing: border-box; }
  html, body {
    width: 873px; height: 1200px; overflow: hidden;
    background: var(--page);
    font-family: "Poppins", sans-serif;
    color: var(--ink);
  }
  .label {
    position: absolute; left: 26px; top: 353px;
    width: 820px; height: 494px;
    background: var(--label);
    box-shadow: 0 2px 8px rgba(0,0,0,0.18);
    overflow: hidden;
  }
  .wash {
    position: absolute; left: 0; top: 0; width: 640px; height: 488px;
    background: linear-gradient(90deg, rgba(205,242,244,0) 0%, var(--wash) 35%, var(--wash) 55%, rgba(205,242,244,0) 100%);
  }
  .brand {
    position: absolute; left: 124px; top: 40px;
    font-weight: 400; font-size: 48px; line-height: 1; letter-spacing: 0.5px;
  }
  .brand sup { font-size: 10px; vertical-align: 28px; margin-left: 1px; }
  .product-name {
    position: absolute; left: 62px; top: 140px; width: 292px;
    font-family: "Kaushan Script", cursive;
    font-size: 76px; line-height: 1; text-align: center;
    white-space: nowrap; -webkit-text-stroke: 1.6px var(--ink);
  }
  .cure-band {
    position: absolute; left: 64px; top: 232px;
    width: 283px; height: 29px;
    background: var(--violet);
    color: #fff; font-size: 19px; font-weight: 400;
    letter-spacing: 3.6px; line-height: 29px; text-align: center;
  }
  .shade-mark {
    position: absolute; left: 160px; top: 279px;
    width: 90px; height: 84px; border-radius: 42px;
    background: var(--splash);
  }
  .shade-number {
    position: absolute; left: 160px; top: 299px; width: 90px;
    text-align: center; color: #fff; font-size: 30px; line-height: 40px; font-weight: 400;
  }
  .volume {
    position: absolute; left: 130px; top: 398px;
    font-size: 17px; line-height: 22px; font-weight: 400;
  }
  .vegan-mark {
    position: absolute; left: 254px; top: 390px;
    width: 38px; height: 38px; border-radius: 50%;
    background: var(--leaf);
  }
  .divider {
    position: absolute; left: 114px; top: 439px;
    width: 184px; height: 1px; background: var(--rule);
  }
  .finish {
    position: absolute; left: 114px; top: 450px; width: 184px;
    text-align: center; font-size: 16px; line-height: 20px; letter-spacing: 3px;
  }
  .info {
    position: absolute; left: 467px; top: 52px; width: 297px;
    font-size: 11px; line-height: 13.8px; letter-spacing: -0.15px;
    text-align: justify; hyphens: auto;
  }
  .info p { margin-bottom: 19px; }
  .info strong { font-weight: 600; }
  .safety-icons {
    position: absolute; left: 467px; top: 374px;
    display: flex; gap: 3px;
  }
  .safety-icons span {
    width: 29px; height: 29px; border-radius: 50%;
    border: 1.2px solid var(--ink);
  }
  .address {
    position: absolute; left: 467px; top: 418px;
    font-size: 9.4px; line-height: 11.6px;
  }
  .origin {
    position: absolute; left: 617px; top: 372px;
    font-size: 11.6px; line-height: 14px;
  }
  .code-panel {
    position: absolute; left: 617px; top: 389px;
    width: 146px; height: 61px; background: var(--panel-grey);
  }
  .base-band {
    position: absolute; left: 0; bottom: 0;
    width: 100%; height: 6px; background: var(--lavender);
  }
</style>
</head>
<body>
  <main class="label">
    <div class="wash" role="img" aria-label="Soft aqua watercolour wash background"></div>

    <div class="brand">velmora<sup>TM</sup></div>
    <div class="product-name">Base Caot</div>
    <div class="cure-band">SOAK OFF UV/LED</div>

    <div class="shade-mark" role="img" aria-label="Blue and violet watercolour splash behind shade number"></div>
    <div class="shade-number">01</div>

    <div class="volume">15ml ℮ 0.5oz</div>
    <div class="vegan-mark" role="img" aria-label="Green leaves vegan symbol"></div>
    <div class="divider"></div>
    <div class="finish">FLEXIBLE</div>

    <section class="info">
      <p><strong>DIRECTIONS FOR USE (ENG):</strong> Velmora Base Coat must be applied in thin layers and cured in one of our Velmora Lamps. See instructions for more information.</p>
      <p><strong>ANVENDELSE (DK):</strong> Velmora Base Coat skal påføres i tynde lag og hærdes i en af vores Velmora Lamper. Se instruktioner for mere information</p>
      <p><strong>CAUTION (ENG):</strong> Keep out of reach of children. Discontinue use if irritation occurs. Avoid direct sunlight or extreme exposure to LED or UV light.</p>
      <p><strong>ADVARSEL (DK):</strong> Opbevar utilgængeligt for børn. Stop Vegan Formula din behandling, hvis produktet forudsager irritation. Undgå direkte sollys eller udsættelse for LED eller UV.</p>
      <p><strong>INGREDIENTS</strong></p>
    </section>

    <div class="safety-icons" aria-label="Safety and disposal marks">
      <span></span><span></span><span></span><span></span>
    </div>
    <div class="address">Nordlys Partners A/S -<br>Lindevej 14C<br>2700 Norby, Denmark</div>
    <div class="origin">Made in Germany</div>
    <div class="code-panel"></div>

    <div class="base-band"></div>
  </main>
</body>
</html>
```